Offshore Energy Projects Management Consultancy needs a business card design

Logo available. We provide teams to deliver engineering consultancy, project management and delivery teams mainly in the offshore renewables sector. The company is all about bringing the right people to a project to deliver the scope.

The business card will be used for all staff.

The business card should be quite simple, vibrant and uncluttered but convey experience, enthusiasm and integration.

Target Market(s)

Energy Project Developers and Tier 1 construction companies

Contact Information for Business Card

Logo should be on the back of the card. I'm happy for the designer to play with the colour of the logo and background colour.

Front of the card should convey all the must have information in a clear and professional manner but without being overly traditional.

Colors

Designer to choose colors to be used in the design.

Requirements
Must have
• Land Line Tel Number, Mobile Tel Number, Email, business address, web address.

```html
<!DOCTYPE html>
<html lang="en">
<head>
<meta charset="utf-8">
<title>Tidewater Delivery Partners – Business Card</title>
<link href="https://fonts.googleapis.com/css2?family=Open+Sans:wght@400;600&display=swap" rel="stylesheet">
<style>
  :root {
    --canvas-bg: #e6e7e8;
    --card-white: #ffffff;
    --brand-blue: #327cc0;
    --brand-blue-light: #3ba4e0;
    --ink: #3a3a3a;
    --on-blue: #ffffff;
  }
  * { margin: 0; padding: 0; box-sizing: border-box; }
  html, body {
    width: 1200px;
    height: 1200px;
    overflow: hidden;
    background: var(--canvas-bg);
    font-family: "Open Sans", Arial, sans-serif;
  }
  .card {
    position: absolute;
    left: 326px;
    width: 546px;
    height: 302px;
  }
  .card--front { top: 188px; background: var(--card-white); }
  .card--back  { top: 708px; background: var(--brand-blue); }

  .name-band {
    position: absolute;
    left: 0;
    top: 50px;
    width: 192px;
    height: 46px;
    background: var(--brand-blue);
    color: var(--on-blue);
    text-align: center;
  }
  .name-band__name {
    display: block;
    font-size: 28px;
    line-height: 30px;
    padding-top: 1px;
    font-weight: 400;
  }
  .name-band__title {
    display: block;
    font-size: 9px;
    letter-spacing: 5px;
    line-height: 12px;
    padding-left: 5px;
  }

  .front-brand {
    position: absolute;
    left: 232px;
    top: 112px;
    width: 290px;
    display: flex;
    align-items: center;
    gap: 10px;
    color: var(--brand-blue);
    font-weight: 600;
    font-size: 21px;
    line-height: 25px;
  }
  .brand-square {
    flex: 0 0 auto;
    width: 18px;
    height: 18px;
    background: var(--brand-blue);
  }

  .contacts {
    position: absolute;
    left: 28px;
    top: 175px;
    list-style: none;
  }
  .contacts__item {
    display: flex;
    align-items: center;
    height: 26px;
    font-size: 20px;
    color: var(--ink);
  }
  .contacts__icon {
    width: 18px;
    height: 18px;
    margin-right: 9px;
    fill: none;
    stroke: var(--brand-blue);
    stroke-width: 1.6;
  }
  .contacts__icon--solid { fill: var(--brand-blue); stroke: none; }

  .back-brand {
    position: absolute;
    left: 0;
    right: 0;
    top: 118px;
    display: flex;
    justify-content: center;
    align-items: center;
    gap: 14px;
    color: var(--on-blue);
    font-weight: 600;
    font-size: 30px;
    letter-spacing: 0.5px;
  }
  .back-brand .brand-square { width: 24px; height: 24px; background: var(--on-blue); }
</style>
</head>
<body>

<section class="card card--front">
  <div class="name-band">
    <span class="name-band__name">YourName</span>
    <span class="name-band__title">TITLE</span>
  </div>

  <div class="front-brand">
    <span class="brand-square"></span>
    <span>TIDEWATER DELIVERY PARTNERS</span>
  </div>

  <ul class="contacts">
    <li class="contacts__item">
      <svg class="contacts__icon" viewBox="0 0 18 18"><rect x="5" y="1" width="8" height="16" rx="1"/><line x1="5" y1="13.5" x2="13" y2="13.5"/></svg>
      +1234567890
    </li>
    <li class="contacts__item">
      <svg class="contacts__icon contacts__icon--solid" viewBox="0 0 18 18"><path d="M4 1.5l3 3-1.5 2c1 2 2.5 3.5 4.5 4.5l2-1.5 3 3-2 2.5C7.5 14.5 3.5 10.5 1.5 4z"/></svg>
      +1234567890
    </li>
    <li class="contacts__item">
      <svg class="contacts__icon contacts__icon--solid" viewBox="0 0 18 18"><path d="M2 4h14v10H2z M2.5 4.5L9 10l6.5-5.5" /><path d="M2 4l7 6 7-6" fill="none" stroke="#fff" stroke-width="1.2"/></svg>
      yourmail@mail.com
    </li>
    <li class="contacts__item">
      <svg class="contacts__icon" viewBox="0 0 18 18"><circle cx="9" cy="9" r="7"/><ellipse cx="9" cy="9" rx="3" ry="7"/><line x1="2" y1="9" x2="16" y2="9"/></svg>
      www.yoursite.com
    </li>
  </ul>
</section>

<section class="card card--back">
  <div class="back-brand">
    <span class="brand-square"></span>
    <span>TIDEWATER DELIVERY PARTNERS</span>
  </div>
</section>

</body>
</html>
```